International printing supplier needs full stationery design

We would like a full stationery design to line up with our new logo and branding.
(In order to symbolise our responsiveness and fast service in the logo, we used an arrow as the accent on the “e“ in the company name.)

What designs we are looking for:
-font to be used in all documentation
-letterhead
-business card
-envelope TC4 (229x324 mm) and LC6 (114x162 mm)
-fax header
-email header
-smaller product labels (69x36mm and 104x73mm)
-bigger product label (A5)
-logo for email signature
-rubber stamp pattern
-flag pattern

Our company (Vóra) is B2B and is based in Central Europe. We operate in the printing press industry supplying press rooms with inks, additives and professional advice.

The design should thus communicate professionalism, responsiveness and swiftness.

Our current logo is attached and our main branding is based around the following colours:
Dark grey: RAL 7016
Orange: RAL 2004 (close to PMS 1655)
Light grey: RAL 9006 (or Pantone Cool Gray 10)

The Look and Feel Slider below should aid anyone in terms of what we imagined the stationery to look like.

Industry/Entity Type

Business

Requirements
Must have
• Logo should be clearly visible on all elements.

The designed or chosen font should match the logo's font and it should be easy to read.

The bigger product label must have an area coloured orange, which needs to contain (maximum 4) industry standard hazard symbols by law. Therefore, these legal constraints need to be included in the design of the product labels. It would be ideal if they could be integrated with the company's orange colour scheme and the rest of the stationery.
Nice to have
• The logo and slogan (Fényes lendülettel!®) should be presented together on all of the proposed designs.

The arrow in the logo would be an ideal symbol to use across the different elements.

The designs should be similar for all the different stationery elements, communicating a clear image and professionalism.
Should not have
• Expensive or impractical solutions in elements of the stationery (i.e. cut-outs, metallic font colours, special materials etc.) should be avoided.

Too many colours on each of the elements of the stationery are not needed, keep it simple.

```html
<!DOCTYPE html>
<html lang="en">
<head>
<meta charset="utf-8">
<title>Vóra business card</title>
<link rel="stylesheet" href="https://fonts.googleapis.com/css2?family=Questrial&display=swap">
<style>
  :root {
    --backdrop: #dcdcdc;
    --card-white: #f4f4f3;
    --brand-orange: #d4501f;
    --text-grey: #55585c;
    --tab-grey: #a9abad;
  }
  html, body {
    margin: 0;
    padding: 0;
    width: 1200px;
    height: 961px;
    overflow: hidden;
    background: var(--backdrop);
    font-family: "Questrial", "Century Gothic", sans-serif;
  }
  .stage {
    position: relative;
    width: 1200px;
    height: 961px;
  }
  .card {
    position: absolute;
    width: 580px;
    height: 330px;
    border-radius: 28px;
    box-shadow: 0 6px 18px rgba(0,0,0,0.18);
    overflow: hidden;
  }
  .card--front {
    left: 140px;
    top: 120px;
    background: var(--card-white);
    color: var(--text-grey);
  }
  .card--back {
    left: 480px;
    top: 500px;
    background: var(--brand-orange);
    color: #ffffff;
  }
  .edge-tab {
    position: absolute;
    width: 12px;
    height: 24px;
  }
  .edge-tab--left { left: 0; top: 200px; background: var(--brand-orange); }
  .edge-tab--right { right: 0; top: 66px; background: var(--tab-grey); }

  .wordmark {
    position: absolute;
    margin: 0;
    font-weight: 400;
    line-height: 1;
    letter-spacing: 2px;
  }
  .card--front .wordmark {
    left: 62px;
    top: 82px;
    font-size: 92px;
    color: var(--brand-orange);
  }
  .slogan {
    position: absolute;
    margin: 0;
    font-size: 21px;
  }
  .card--front .slogan {
    right: 40px;
    top: 58px;
  }
  .holder {
    position: absolute;
    right: 40px;
    top: 150px;
    text-align: right;
  }
  .holder__name {
    margin: 0;
    font-size: 14px;
    letter-spacing: 1px;
    font-weight: 700;
  }
  .holder__role {
    margin: 2px 0 0;
    font-size: 13px;
    color: var(--brand-orange);
  }
  .contact {
    position: absolute;
    left: 70px;
    top: 200px;
    font-size: 12.5px;
    line-height: 1.35;
  }
  .contact__address { margin: 0 0 10px; }
  .contact__list { margin: 0; padding: 0; list-style: none; }
  .contact__label { color: var(--brand-orange); font-weight: 700; }

  .back-lockup {
    position: absolute;
    inset: 0;
    display: flex;
    flex-direction: column;
    align-items: center;
    justify-content: center;
  }
  .card--back .wordmark {
    position: static;
    font-size: 110px;
    color: #ffffff;
  }
  .card--back .slogan {
    position: static;
    margin-top: 6px;
    font-size: 25px;
  }
</style>
</head>
<body>
<main class="stage">
  <section class="card card--front" aria-label="Business card front">
    <span class="edge-tab edge-tab--left"></span>
    <span class="edge-tab edge-tab--right"></span>
    <p class="slogan">Fényes lendülettel!®</p>
    <h1 class="wordmark">Vóra</h1>
    <div class="holder">
      <p class="holder__name">MARTA KELLER</p>
      <p class="holder__role">Managing director</p>
    </div>
    <address class="contact" style="font-style: normal;">
      <p class="contact__address">14 Linden Row<br>Harwick Vale, HV3 7QP</p>
      <ul class="contact__list">
        <li><span class="contact__label">T:</span> 07700 900 418</li>
        <li><span class="contact__label">F:</span> 07700 900 418</li>
        <li><span class="contact__label">M:</span> 07700 900 418</li>
        <li><span class="contact__label">E:</span> info@vora-ink.com</li>
        <li><span class="contact__label">W:</span> www.vora-ink.com</li>
      </ul>
    </address>
  </section>

  <section class="card card--back" aria-label="Business card back">
    <div class="back-lockup">
      <p class="wordmark">Vóra</p>
      <p class="slogan">Fényes lendülettel!®</p>
    </div>
  </section>
</main>
</body>
</html>
```